Webpage Needed for Bright Harbor Wiring Electrical and Security

We need a web design for our company showing people we arent just a small business. We want to look big so people can trust us. I would like information from my business cards on the page. example, we do all house rennovations, construction, commercial, 24 hour emergency service, new installations, repairs, maintenance, home theatre and so on...

I would also like images from my facebook on the page and linked. facebook.com/brightharborwiring

Target Market(s)

builders, residents,

Industry/Entity Type

Business

Number of Pages Required

1 page

Font styles to use
Other font styles liked:
• Juice bold

Requirements
Must have
• colours the same as the logo. background must be white. also the font must be Juice Bold which is the font of the logo
Should not have
• black as the background

```html
<!DOCTYPE html>
<html lang="en">
<head>
<meta charset="utf-8">
<title>Bright Harbor Wiring Electrical and Security</title>
<link href="https://fonts.googleapis.com/css2?family=Baumans&family=Electrolize&display=swap" rel="stylesheet">
<style>
:root{
  --blue:#4bbfea;
  --orange:#f48a4a;
  --ink:#1c1c1c;
  --text:#2a2a2a;
  --muted:#8a8a8a;
  --line:#dcdcdc;
  --panel:#f3f3f3;
  --white:#ffffff;
  --footer:#000000;
}
*{margin:0;padding:0;box-sizing:border-box}
html,body{width:669px;height:1200px;overflow:hidden;background:var(--white)}
body{position:relative;font-family:"Electrolize",sans-serif;color:var(--text)}
.abs{position:absolute}

/* header */
.site-header{left:0;top:0;width:669px;height:49px;background:var(--white);z-index:3}
.brand-tab{left:41px;top:0;width:88px;height:64px;background:var(--white);border-radius:0 0 14px 14px;box-shadow:0 2px 3px rgba(0,0,0,.15);z-index:4;text-align:center;padding-top:6px}
.brand-name{font-family:"Baumans",sans-serif;font-size:14px;line-height:13px;color:var(--ink)}
.brand-tag{font-size:6px;color:var(--ink);margin-top:3px}
.phone{right:52px;top:9px;font-family:"Baumans",sans-serif;font-size:15px;color:var(--blue);display:flex;align-items:center;gap:4px}
.main-nav{right:52px;top:30px;display:flex;gap:18px;font-size:7.5px;letter-spacing:.4px;color:var(--ink)}
.main-nav .current{color:var(--orange)}

/* hero */
.hero{left:0;top:49px;width:669px;height:264px;background:linear-gradient(160deg,#6d6a66 0%,#8c7b64 45%,#b08a55 75%,#5a5049 100%)}
.hero-caption{left:0;top:225px;width:669px;height:39px;background:rgba(20,20,20,.82)}
.hero-title{left:52px;top:6px;font-family:"Baumans",sans-serif;font-size:23px;color:var(--white);letter-spacing:.3px}
.hero-dots{right:52px;top:10px;display:flex;gap:2px}
.dot{width:4px;height:4px;border-radius:50%;background:#b5b5b5}
.dot.on{background:var(--orange)}
.hero-more{right:52px;top:20px;font-size:7px;color:var(--white);text-decoration:underline;font-style:italic}

/* section headings */
.section-title{font-family:"Baumans",sans-serif;font-weight:400;font-size:16px;letter-spacing:1px;color:var(--ink);padding-bottom:3px;border-bottom:1px solid var(--line)}
.section-title span{color:var(--blue)}
.section-title span.warm{color:var(--orange)}

.btn-pill{display:inline-block;height:14px;padding:0 9px;border:1px solid #cfcfcf;border-radius:4px;background:linear-gradient(#fafafa,#e4e4e4);font-size:6px;font-style:italic;color:#666;line-height:13px}

/* who we are */
.about-title{left:51px;top:340px;width:568px}
.about-copy{left:51px;top:369px;width:411px;font-size:7.2px;line-height:11.8px;color:var(--text)}
.about-photo{left:472px;top:371px;width:147px;height:108px;background:linear-gradient(120deg,#5e6468 0%,#9aa6ae 50%,#dfe4e8 100%)}
.about-btn{left:51px;top:471px}

/* divider with brand badge */
.grey-band{left:0;top:558px;width:669px;height:282px;background:var(--panel);border-top:1px solid var(--line);border-bottom:1px solid var(--line)}
.divider-badge{left:290px;top:512px;width:89px;height:61px;background:var(--white);border-radius:0 0 14px 14px;border:1px solid var(--line);border-top:none;text-align:center;padding-top:6px;z-index:2}

/* what we do */
.services-title{left:51px;top:590px;width:568px}
.service{top:621px;width:128px}
.service-img{width:128px;height:73px}
.service-bar{height:3px}
.service h3{font-family:"Baumans",sans-serif;font-weight:400;font-size:10.5px;line-height:11.5px;letter-spacing:.4px;color:var(--ink);margin-top:6px;height:24px}
.service p{font-size:6.4px;line-height:9.3px;color:var(--text);height:42px}
.slide-arrow{top:688px}
.services-dots{left:320px;top:805px;display:flex;gap:2px}

/* clients */
.clients-title{left:51px;top:866px;width:372px}
.client-photo{left:51px;top:897px;width:77px;height:77px;border-radius:50%;border:2px solid var(--orange);background:radial-gradient(circle at 50% 40%,#d9c3ad,#8ea3b8 60%,#dfe5ea)}
.quote-mark{left:130px;top:896px;font-family:"Baumans",sans-serif;font-size:20px;color:#c9c9c9}
.quote-text{left:145px;top:904px;width:276px;font-size:7.2px;line-height:10.6px;font-style:italic;color:var(--text)}
.quote-author{left:145px;top:961px;font-size:7.5px;color:var(--ink)}
.clients-btn{left:51px;top:985px}

/* contact */
.contact-box{left:442px;top:869px;width:177px;height:148px;border:1px solid #d8d8d8;border-radius:8px;background:linear-gradient(#ffffff 30%,#e6e6e6)}
.contact-box .section-title{position:absolute;left:8px;top:8px;width:160px;font-size:13px}
.field{position:absolute;left:8px;width:162px;background:var(--white);border:1px solid #ececec;font-size:6px;color:#999;padding:4px 5px}
.send{position:absolute;left:8px;top:118px;width:93px;height:19px;border-radius:4px;background:var(--blue);color:var(--white);font-size:8.5px;font-style:italic;line-height:19px;padding-left:10px}

/* footer */
.site-footer{left:0;top:1059px;width:669px;height:141px;background:var(--footer)}
.to-top{left:320px;top:1048px;width:30px;height:14px}
.footer-brand{left:0;top:1078px;width:669px;text-align:center}
.footer-brand .brand-name{color:#9a9a9a;font-size:16px;line-height:15px}
.footer-brand .brand-tag{color:#9a9a9a}
.footer-nav{left:0;top:1140px;width:669px;display:flex;justify-content:center;gap:10px;font-size:7.5px;letter-spacing:.5px;color:#bdbdbd}
.social{left:0;top:1155px;width:669px;display:flex;justify-content:center;gap:3px}
.social span{width:15px;height:15px;border-radius:50%;background:#8c8c8c}
.copyright{left:0;top:1174px;width:669px;text-align:center;font-size:5.5px;color:#9a9a9a}
</style>
</head>
<body>

<header class="abs site-header">
  <div class="abs phone">
    <svg width="14" height="14" viewBox="0 0 14 14" aria-hidden="true"><circle cx="7" cy="7" r="6.2" fill="none" stroke="#4bbfea" stroke-width="1.2"/><path d="M5 3.8 L6.2 5.6 L5.5 6.4 Q6.3 8 7.7 8.6 L8.5 7.8 L10.2 9 Q9.8 10.4 8.6 10.3 Q4.2 9.4 3.7 5.3 Q3.8 4 5 3.8Z" fill="#4bbfea"/></svg>
    0412 555 308
  </div>
  <nav class="abs main-nav">
    <span class="current">HOME</span><span>ABOUT US</span><span>SERVICES</span><span>TESTIMONIALS</span><span>CONTACT</span>
  </nav>
</header>
<div class="abs brand-tab">
  <div class="brand-name">Bright<br>Harbor<br>Wiring</div>
  <div class="brand-tag">electrical and security</div>
</div>

<section class="abs hero" role="img" aria-label="Construction site interior with electricians in hi-vis vests, a scissor lift and stacked building materials">
  <div class="abs hero-caption">
    <div class="abs hero-title">Electrical Installations</div>
    <div class="abs hero-dots"><i class="dot on"></i><i class="dot"></i><i class="dot"></i><i class="dot"></i><i class="dot"></i></div>
    <div class="abs hero-more">learn more »</div>
  </div>
</section>

<h2 class="abs section-title about-title">WHO <span>WE ARE</span></h2>
<p class="abs about-copy">Lorem ipsum dolor sit amet, consectetur adipiscing elit. Cras sodales sapien sed lacus bibendum scelerisque. Nulla et sem auctor, tempus quam quis, accumsan mi. Aliquam quis dictum purus. Integer id aliquam libero. Fusce odio nulla, viverra at bibendum vel, euismod nec velit. In lacinia consequat venenatis. Nullam finibus sollicitudin ultricies. Aenean quis dictum diam, ut tempor justo. Pellentesque habitant morbi tristique senectus et netus et malesuada fames ac turpis egestas. Etiam vel nunc nunc. Vestibulum bibendum ex a dui ultrices, sit amet rhoncus est accumsan. Vestibulum id bibendum sem. Aliquam eros augue, luctus eget bibendum id, luctus eget neque. Nunc cursus interdum elit. Phasellus vehicula tellus ac viverra interdum. Sed sapien lectus, molestie sit amet pretium ut, ornare vitae ligula. Pellentesque ornare pretium leo. Nullam in augue eu neque hendrerit imperdiet non vitae erat muris eu.</p>
<div class="abs about-photo" role="img" aria-label="Electrician in a company shirt fitting a ceiling light"></div>
<span class="abs btn-pill about-btn">Learn more »</span>

<div class="abs grey-band"></div>
<div class="abs divider-badge">
  <div class="brand-name">Bright<br>Harbor<br>Wiring</div>
  <div class="brand-tag">electrical and security</div>
</div>

<h2 class="abs section-title services-title">WHAT <span>WE DO</span></h2>

<svg class="abs slide-arrow" style="left:30px" width="12" height="30" viewBox="0 0 12 30" aria-hidden="true"><path d="M10 1 L2 15 L10 29" fill="none" stroke="#b0b0b0" stroke-width="1.3"/></svg>
<svg class="abs slide-arrow" style="left:627px" width="12" height="30" viewBox="0 0 12 30" aria-hidden="true"><path d="M2 1 L10 15 L2 29" fill="none" stroke="#b0b0b0" stroke-width="1.3"/></svg>

<article class="abs service" style="left:51px">
  <div class="service-img" role="img" aria-label="White company service van parked outside" style="background:linear-gradient(135deg,#e9eef2,#bfc6cc 55%,#3d3f42)"></div>
  <div class="service-bar" style="background:var(--blue)"></div>
  <h3>24 Hour Emergency Service</h3>
  <p>Sed sapien lectus, molestie sit amet pretium ut, ornare vitae ligula. Pellentes que ornare pretium leo. Nullam in augue eu neque hendrerit.</p>
  <span class="btn-pill">Learn more »</span>
</article>
<article class="abs service" style="left:197px">
  <div class="service-img" role="img" aria-label="Gloved hand holding a clamp meter on colourful cables" style="background:linear-gradient(135deg,#d9642c,#5a3a2e 50%,#2b2b2b)"></div>
  <div class="service-bar" style="background:var(--orange)"></div>
  <h3>New Electrical Installations</h3>
  <p>Nullam pellentesque placerat mollis. Class aptent taciti sociosqu ad litora torquent per conubia nostra, per incept himenaeos aliquam cursus porttitor.</p>
  <span class="btn-pill">Learn more »</span>
</article>
<article class="abs service" style="left:344px">
  <div class="service-img" role="img" aria-label="Renovated meeting room with warm pendant lighting" style="background:linear-gradient(135deg,#4a3a2a,#d7a45a 50%,#2d2620)"></div>
  <div class="service-bar" style="background:var(--orange)"></div>
  <h3>House Renovations / Extensions</h3>
  <p>Phasellus vitae felis ut mauris pulvinar interdum non vel sem. In tristique quam sit amet dui porttitor maximus. Vivamus tempus ultricies.</p>
  <span class="btn-pill">Learn more »</span>
</article>
<article class="abs service" style="left:491px">
  <div class="service-img" role="img" aria-label="Home theatre room with projection screen and lounge seating" style="background:linear-gradient(135deg,#3b3733,#7a6a58 45%,#1e1c1a)"></div>
  <div class="service-bar" style="background:var(--orange)"></div>
  <h3>Home Theater &amp; Surround Sound</h3>
  <p>Donec ut felis eget lectus pulvinar tincidunt ac eu felis. Aliquam aliquet eros sed ultricies pharetra. Cras at purus fermentum, auctor felis eget.</p>
  <span class="btn-pill">Learn more »</span>
</article>

<div class="abs services-dots"><i class="dot on"></i><i class="dot"></i><i class="dot"></i><i class="dot"></i><i class="dot"></i></div>

<h2 class="abs section-title clients-title">OUR <span>HAPPY</span> <span class="warm">CLIENTS</span></h2>
<div class="abs client-photo" role="img" aria-label="Portrait of a smiling client in a suit"></div>
<div class="abs quote-mark">“</div>
<p class="abs quote-text">Lorem ipsum dolor sit amet, consectetur adipiscing elit. Cras sodales sapien sed lacus bibendum scelerisque. Nulla et sem auctor, tempus quam quis, accumsan mi. Aliquam quis dictum purus. Integer id aliquam libero. Fusce odio nulla, viverrag at bibendum vel, euismod nec velit. In lacinia consequat. venenatis. Nullam finibus sollicitudin ultricies. Aenean quis dictum diam, ut tempor justo.</p>
<div class="abs quote-author">— Martin Ellsworth, Ellsworth Homes</div>
<span class="abs btn-pill clients-btn">View all testimonials »</span>

<form class="abs contact-box">
  <h2 class="section-title">GET <span>IN TOUCH</span></h2>
  <div class="field" style="top:30px;height:19px">name</div>
  <div class="field" style="top:52px;height:19px">email</div>
  <div class="field" style="top:74px;height:39px">message</div>
  <div class="send">Send a message »</div>
</form>

<footer class="abs site-footer"></footer>
<svg class="abs to-top" viewBox="0 0 30 14" aria-hidden="true"><path d="M0 14 L15 0 L30 14Z" fill="#000"/><path d="M15 4 V13 M11 8 L15 4 L19 8" stroke="#fff" stroke-width="1.6" fill="none"/></svg>
<div class="abs footer-brand">
  <div class="brand-name">Bright<br>Harbor<br>Wiring</div>
  <div class="brand-tag">electrical and security</div>
</div>
<nav class="abs footer-nav">
  <span>HOME</span><span>|</span><span>ABOUT US</span><span>|</span><span>SERVICES</span><span>|</span><span>TESTIMONIALS</span><span>|</span><span>CONTACT</span>
</nav>
<div class="abs social"><span aria-label="Social profile link"></span><span aria-label="Social profile link"></span><span aria-label="Social profile link"></span></div>
<div class="abs copyright">©2015 Bright Harbor Wiring Electrical and Security.</div>

</body>
</html>
```